" Sou cirurgiao plástico e tudo seria para o meu consultório particular, estou iniciando minhas atividades em Americana/SP, onde me mudei há 6 meses, mas já sou formado há 4 anos. "

```html
<!DOCTYPE html>
<html lang="pt-BR">
<head>
<meta charset="UTF-8">
<title>Dr. Marcos Felder – Cartão de Visita</title>
<link href="https://fonts.googleapis.com/css2?family=Marcellus&family=Arimo:wght@400;700&display=swap" rel="stylesheet">
<style>
  :root {
    --bg: #e9e6e1;
    --white: #ffffff;
    --teal: #2f8f98;
    --teal-dark: #237b84;
    --teal-light: #7cc7cc;
    --ink: #4a4a4a;
  }
  * { margin: 0; padding: 0; box-sizing: border-box; }
  html, body { width: 1200px; height: 1200px; overflow: hidden; }
  body { background: var(--bg); position: relative; font-family: "Arimo", Arial, sans-serif; }

  .card { position: absolute; box-shadow: 0 10px 24px rgba(0,0,0,.22); overflow: hidden; }

  /* Front */
  .card-front { left: 264px; top: 223px; width: 624px; height: 396px; background: var(--white); }
  .front-mark {
    position: absolute; top: 52px; left: 0; width: 100%; text-align: center;
    font-family: "Marcellus", Georgia, serif; font-size: 92px; color: var(--teal); line-height: 1;
  }
  .front-name {
    position: absolute; top: 196px; width: 100%; text-align: center;
    font-family: "Marcellus", Georgia, serif; font-size: 42px; color: var(--ink); letter-spacing: 1px;
  }
  .front-role {
    position: absolute; top: 254px; width: 100%; text-align: center;
    font-family: "Marcellus", Georgia, serif; font-size: 17px; color: var(--teal); letter-spacing: 4px;
  }
  .front-wave { position: absolute; left: 0; bottom: 0; width: 100%; height: 80px; }

  /* Back */
  .card-back { left: 324px; top: 643px; width: 708px; height: 401px; background: var(--teal); color: var(--white); }
  .back-mark {
    position: absolute; right: 30px; top: 20px;
    font-family: "Marcellus", Georgia, serif; font-size: 300px; line-height: 1;
    color: rgba(255,255,255,.13);
  }
  .back-head { position: absolute; left: 34px; top: 30px; width: 400px; }
  .back-name { font-size: 23px; font-weight: 700; }
  .back-name .crm { font-size: 15px; font-weight: 400; }
  .back-rule { height: 1px; background: rgba(255,255,255,.7); margin: 6px 0 5px; }
  .back-spec { font-size: 9.5px; letter-spacing: .2px; }
  .back-bio { position: absolute; left: 34px; top: 110px; font-size: 16px; line-height: 1.3; }
  .back-contacts { position: absolute; left: 34px; top: 206px; font-size: 17px; }
  .contact { display: flex; align-items: flex-start; gap: 8px; line-height: 1.25; margin-bottom: 4px; }
  .contact.email { font-weight: 700; }
  .contact svg { flex: none; width: 15px; height: 15px; margin-top: 3px; }
  .address { margin-top: 6px; }
  .address strong { display: block; }
</style>
</head>
<body>
  <section class="card card-front">
    <div class="front-mark">MF</div>
    <div class="front-name">DR. MARCOS FELDER</div>
    <div class="front-role">CIRURGIÃO PLÁSTICO</div>
    <svg class="front-wave" viewBox="0 0 624 80" preserveAspectRatio="none">
      <defs>
        <linearGradient id="waveFill" x1="0" x2="1" y1="0" y2="0">
          <stop offset="0" stop-color="#3a9aa3"/>
          <stop offset="1" stop-color="#6fc0c6"/>
        </linearGradient>
      </defs>
      <path d="M0 40 C 150 10, 330 10, 624 28 L624 80 L0 80 Z" fill="#cfe9eb"/>
      <path d="M0 52 C 170 22, 350 26, 624 40 L624 80 L0 80 Z" fill="url(#waveFill)"/>
      <path d="M0 66 C 200 46, 400 48, 624 58 L624 80 L0 80 Z" fill="var(--teal-dark)" opacity=".6"/>
    </svg>
  </section>

  <section class="card card-back">
    <div class="back-mark">MF</div>
    <div class="back-head">
      <div class="back-name">Dr. Marcos Felder <span class="crm">- CRM/SP 204.318</span></div>
      <div class="back-rule"></div>
      <div class="back-spec">CIRURGIA PLÁSTICA | ESTÉTICA E REPARADORA | MICROCIRURGIA</div>
    </div>
    <div class="back-bio">
      - Formado na Fac. Medicina da UFSR<br>
      - Residência no Hosp. Clínicas da FMSR
    </div>
    <div class="back-contacts">
      <div class="contact">
        <svg viewBox="0 0 16 16"><path d="M4 1 L6 5 L4.5 6.5 C5.5 8.8 7.2 10.5 9.5 11.5 L11 10 L15 12 L13.5 15 C7 14.5 1.5 9 1 2.5 Z" fill="#fff"/></svg>
        <span>(19) 3555-0142/ 3555-0187</span>
      </div>
      <div class="contact email">
        <svg viewBox="0 0 16 16"><rect x="1" y="3" width="14" height="10" fill="#fff"/><path d="M1 3 L8 9 L15 3" fill="none" stroke="#2f8f98" stroke-width="1.4"/></svg>
        <span>drmarcosfelder@email.com</span>
      </div>
      <div class="contact">
        <svg viewBox="0 0 16 16"><circle cx="8" cy="8" r="7" fill="#fff"/></svg>
        <span>www.drmarcosfelder.com.br</span>
      </div>
      <div class="contact address">
        <svg viewBox="0 0 16 16"><path d="M8 1 C4.5 1 2.5 3.5 2.5 6.3 C2.5 10 8 15.5 8 15.5 C8 15.5 13.5 10 13.5 6.3 C13.5 3.5 11.5 1 8 1 Z" fill="#fff"/><circle cx="8" cy="6.3" r="2.2" fill="#2f8f98"/></svg>
        <span><strong>Edifício Aurora</strong>Rua das Palmeiras, 412 Cjto 23<br>Americana - SP - CEP:13470-100</span>
      </div>
    </div>
  </section>
</body>
</html>
```